Marcelo Vantrini
Tenor & Vocal Coach
mvbaritono@quellmail.net
(713) 562-8307
www.voicefromthecore.net
Want two sided postcard / rack card.4" x 9"
Front - vertical - picture in t-shirt, name, title (Tenor & Vocal Coach), contact information
Back - horizontal - picture in jacket, name, title (Tenor & Vocal Coach), contact information, bio (see attachment for words)
Do not leave space for an address.
Looking for an edgy modern design!

Target Market(s)

Young adults

Requirements
Nice to have
• Will pay extra to get a complimentary business card design, two sided

```html
<!DOCTYPE html>
<html lang="en">
<head>
<meta charset="utf-8">
<title>Marcelo Vantrini – Rack Card</title>
<link rel="stylesheet" href="https://fonts.googleapis.com/css2?family=Jost:wght@300;400&display=swap">
<style>
  :root {
    --stage: #353535;
    --accent: #a4e05a;
    --ink: #2a2a2a;
    --paper: #ffffff;
    --white: #ffffff;
    --photo-light: #e8e2d2;
    --photo-mid: #9a9590;
    --photo-dark: #4a4650;
  }
  * { box-sizing: border-box; margin: 0; padding: 0; }
  html, body { width: 1200px; height: 1200px; overflow: hidden; }
  body {
    background: var(--stage);
    font-family: "Jost", "Futura", sans-serif;
    font-weight: 300;
    position: relative;
  }

  /* Front – vertical */
  .card-front {
    position: absolute; left: 70px; top: 132px;
    width: 380px; height: 822px; overflow: hidden;
  }
  .card-front .photo {
    position: absolute; inset: 0;
    background:
      linear-gradient(180deg, rgba(0,0,0,0) 60%, rgba(40,36,50,0.55) 100%),
      linear-gradient(160deg, var(--photo-light) 0%, #d8cfc0 25%, var(--photo-mid) 55%, var(--photo-dark) 100%);
  }
  .card-front .frame {
    position: absolute; left: 26px; top: 39px; width: 328px; height: 757px;
    border: 4px solid var(--accent);
  }
  .card-front .name {
    position: absolute; left: 45px; top: 598px;
    color: var(--white); font-weight: 300; font-size: 54px;
    line-height: 46px; letter-spacing: -1px; text-transform: uppercase;
  }
  .card-front .title {
    position: absolute; left: 45px; top: 698px;
    color: var(--white); font-size: 16px; text-transform: uppercase;
  }
  .card-front .contact {
    position: absolute; left: 45px; top: 728px;
    color: var(--white); font-size: 13px; line-height: 16px; text-transform: uppercase;
    list-style: none;
  }

  /* Back – horizontal */
  .card-back {
    position: absolute; left: 350px; top: 330px;
    width: 814px; height: 374px; overflow: hidden;
    background: var(--paper);
  }
  .card-back .photo {
    position: absolute; left: 0; top: 0; width: 349px; height: 374px;
    background:
      radial-gradient(ellipse at 50% 90%, #2a2e3c 0%, #3a3c48 35%, rgba(0,0,0,0) 60%),
      linear-gradient(160deg, #5a5640 0%, var(--photo-light) 40%, #c9c2b2 70%, #6a6660 100%);
  }
  .card-back .frame {
    position: absolute; left: 26px; top: 26px; width: 762px; height: 322px;
    border: 3px solid var(--accent);
  }
  .card-back .text {
    position: absolute; left: 364px; top: 36px; width: 420px; color: var(--ink);
  }
  .card-back .name {
    font-weight: 300; font-size: 35px; line-height: 30px;
    letter-spacing: -1px; text-transform: uppercase;
  }
  .card-back .title { font-size: 13px; margin-top: 9px; text-transform: uppercase; }
  .card-back .bio { font-size: 11.2px; line-height: 15px; margin-top: 28px; }
  .card-back .cta { font-size: 19px; margin-top: 10px; }
  .card-back .contact {
    list-style: none; font-size: 12.5px; line-height: 16px; margin-top: 5px;
    text-transform: uppercase;
  }
</style>
</head>
<body>
  <section class="card-front">
    <div class="photo" role="img" aria-label="Portrait photo of the singer smiling in a grey t-shirt"></div>
    <div class="frame"></div>
    <h1 class="name">Marcelo<br>Vantrini</h1>
    <p class="title">Tenor &amp; Vocal Coach</p>
    <ul class="contact">
      <li>mvbaritono@quellmail.net</li>
      <li>(713) 562-8307</li>
      <li>www.voicefromthecore.net</li>
    </ul>
  </section>

  <section class="card-back">
    <div class="photo" role="img" aria-label="Portrait photo of the singer in a dark jacket and white shirt"></div>
    <div class="frame"></div>
    <div class="text">
      <h2 class="name">Marcelo<br>Vantrini</h2>
      <p class="title">Tenor &amp; Vocal Coach</p>
      <p class="bio">Marcelo is a local singer and actor who has been working professionally around the country as a concert artist and musical theater performer.<br>He studied at the Brennard School of Music, Bayfield University and works as a vocal coach with local youths and adults in Houston area.<br>Marcelo’s goal is to help his students master their individual instrument so that they can achieve a natural and effortless vocal production.</p>
      <p class="cta">For more information please contact Marcelo today!</p>
      <ul class="contact">
        <li>mvbaritono@quellmail.net</li>
        <li>(713) 562-8307</li>
        <li>www.voicefromthecore.net</li>
      </ul>
    </div>
  </section>
</body>
</html>
```